Chocolate company needing sticker for products

I have a small chocolate company Willow Bend Sweets in Austin Texas. I make all vegan, gluten free, organic, faire trade chocolate that tastes amazing! It is allergy friendly approvable by all ages. I want to have a great sticker that i can put on our boxes and bags. I am using a lot of natural craft color and brown. I am open to color options possibly for different flavors. I want the packaging to reflect the basis of my company. It is all handmade by me but i don't want it to have to much of a crafty look to it. I have attached the logo designs I have. it the sticker can have som of the bullet points about the company that would be great. But it needs to say Locally Made in Austin Texas. it also has to have the company address.
418 West Cobbler Ridge Rd #207 Austin Tx 78745. These things are required by the state for food regulations. I want something that looks great and I can be really proud to put on my product! Thanks so much for all of your help in advance. Dot

I also need some other information added to the sticker. Website which is willowbendsweetsatx.com 

Phone number 512.368.4175. Instagram willowbendsweets. Thanks for your hard work! 

Industry/Entity Type

Chocolate Company

Requirements
Must have
• The logo is added at the bottom as well as designs I like I want to have a professional look but it to be approvable by all consumers. I will gig feed back as i see what designs come through. This will probably fold out into a multi design project so i will be looking for assistance on other areas of this as well. Thanks

```html
<!DOCTYPE html>
<html lang="en">
<head>
<meta charset="utf-8">
<title>Willow Bend Sweets – Product Sticker</title>
<link rel="stylesheet" href="https://fonts.googleapis.com/css2?family=IM+Fell+English&family=Marcellus&family=Marcellus+SC&display=swap">
<style>
  :root {
    --page: #ffffff;
    --kraft: #ead59e;
    --kraft-deep: #e7d090;
    --rust: #cf6230;
    --brick: #cb5a3a;
    --cream: #ffffff;
    --cocoa: #3a2210;
    --seam: #dcc48a;
  }
  * { margin: 0; padding: 0; box-sizing: border-box; }
  html, body { width: 1200px; height: 1000px; overflow: hidden; background: var(--page); }
  .canvas { position: relative; width: 1200px; height: 1000px; }
  .sticker {
    position: absolute; left: 235px; top: 0; width: 728px; height: 1000px;
    background: var(--kraft);
  }
  .fold-line {
    position: absolute; left: 0; right: 0; top: 499px; height: 2px;
    background: var(--seam);
  }
  .product-panel {
    position: absolute; left: 48px; top: 46px; width: 635px; height: 394px;
    background: var(--rust); color: var(--cream); text-align: center;
  }
  .product-name {
    position: absolute; left: 0; right: 0; top: 28px;
    font-family: "IM Fell English", serif; font-weight: 400;
    font-size: 49px; line-height: 64px; letter-spacing: 1px;
  }
  .tagline {
    position: absolute; left: 0; right: 0; top: 170px;
    font-family: "Marcellus SC", serif; font-size: 22px; letter-spacing: 1px;
  }
  .dotted-rule {
    position: absolute; left: 25px; right: 25px; top: 227px; height: 5px;
    background-image: radial-gradient(circle, var(--cocoa) 1.6px, transparent 2px);
    background-size: 6.5px 5px; background-repeat: repeat-x;
  }
  .origin {
    position: absolute; left: 0; right: 0; top: 248px;
    font-family: "Marcellus SC", serif; font-size: 31px; letter-spacing: 0.5px;
  }
  .qualities {
    position: absolute; left: 0; right: 0; top: 306px; height: 76px;
    font-family: "Marcellus", sans-serif; font-size: 20px; line-height: 39px;
  }
  .quality-group { position: absolute; top: 0; width: 180px; margin-left: -90px; }
  .quality-group:nth-of-type(1) { left: 92px; }
  .quality-group:nth-of-type(2) { left: 325px; }
  .quality-group:nth-of-type(3) { left: 548px; }
  .quality-divider {
    position: absolute; top: 29px; width: 12px; height: 26px; margin-left: -6px;
    background: var(--cream);
  }
  .quality-divider.first { left: 205px; }
  .quality-divider.second { left: 444px; }
  .brand-block {
    position: absolute; left: 235px; top: 533px; width: 261px; height: 295px;
    background: var(--kraft-deep); color: var(--brick);
    display: flex; flex-direction: column; align-items: center; justify-content: center;
    font-family: "Marcellus", sans-serif; text-align: center;
  }
  .brand-name { font-size: 50px; line-height: 62px; letter-spacing: 2px; text-transform: uppercase; }
  .ingredients {
    position: absolute; left: 48px; right: 46px; top: 858px;
    font-family: "Marcellus SC", serif; font-size: 16px; line-height: 28px;
    color: var(--cocoa); text-align: justify; letter-spacing: 0.6px;
    text-align-last: left;
  }
  .address {
    position: absolute; left: 0; right: 0; top: 929px;
    font-family: "Marcellus SC", serif; font-size: 27px; color: var(--cocoa);
    text-align: center; letter-spacing: 0.5px;
  }
</style>
</head>
<body>
<div class="canvas">
  <div class="sticker">
    <section class="product-panel">
      <h1 class="product-name">Chocolate Covered<br>Chocolate Chip Cookies</h1>
      <p class="tagline">semi-sweet, always good</p>
      <div class="dotted-rule"></div>
      <p class="origin">Locally Made in Austin, Texas</p>
      <div class="qualities">
        <div class="quality-group">VEGAN<br>GLUTEN FREE</div>
        <div class="quality-group">ORGANIC<br>ALLERGY FREE</div>
        <div class="quality-group">FAIR TRADE<br>DELICIOUS</div>
        <span class="quality-divider first" role="img" aria-label="small decorative ornament"></span>
        <span class="quality-divider second" role="img" aria-label="small decorative ornament"></span>
      </div>
    </section>
    <div class="fold-line"></div>
    <div class="brand-block">
      <p class="brand-name">Willow<br>Bend<br>Sweets</p>
    </div>
    <p class="ingredients">ingredients: cacao, coconut milk, rice milk, mulberry, vanillin, mulberry extract, salt, coloring.</p>
    <p class="address">418 West Cobbler Ridge Rd #207 Austin Tx 78745</p>
  </div>
</div>
</body>
</html>
```